Invitation Design Project

I would like to have a custom invitation (and reception/response cards) designed for my son's Bar Mitzvah. I have a strong idea of what I want and have a few mock-ups, but my "home made" effort would be improved by the addition of professional creativity and skill. The invitation should be white, red, and black, and a bold typographic style (see attachment). I am looking for a clean modern feel, and prefer square shaped invitations. I need the final product in an electronic format that I could either print myself or have done at a local printer.

Target Market(s)

Guests to a Bar Mitzvah. A group of family and friends ranging from 40-60 years of age, and a group of my son's 13 year old friends.

Industry/Entity Type

Electronic

Requirements
Must have
• Square shaped invitation (exact dimensions in attached file)
Typographic style
Red, black, white
Red color should be CMYK: 30-96-76-26
Nice to have
• I like the two icons on my attached sample reception card, especially the swirl/Torah one. I would be nice to use these (or similar ones) if there is a way to do so, but this is not a requirement.

```html
<!DOCTYPE html>
<html lang="en">
<head>
<meta charset="utf-8">
<title>Bar Mitzvah Invitation Suite</title>
<link rel="stylesheet" href="https://fonts.googleapis.com/css2?family=Montserrat:wght@300;400;500&display=swap">
<style>
  :root {
    --red: #c8202f;
    --ink: #1a1a1a;
    --paper: #ffffff;
    --backdrop: #e6e6e6;
    --shadow: rgba(0, 0, 0, 0.45);
  }
  * { margin: 0; padding: 0; box-sizing: border-box; }
  html, body {
    width: 1200px;
    height: 847px;
    overflow: hidden;
    background: var(--backdrop);
    font-family: "Montserrat", "Helvetica Neue", Arial, sans-serif;
  }
  .suite {
    position: relative;
    width: 1200px;
    height: 847px;
  }
  .card {
    position: absolute;
    display: block;
    overflow: visible;
    filter: drop-shadow(5px 6px 4px var(--shadow));
  }
  .card text { font-family: "Montserrat", "Helvetica Neue", Arial, sans-serif; }
  .rsvp-card { left: 96px; top: 82px; transform: rotate(1.5deg); transform-origin: center; }
  .reception-tag { left: 0; top: 380px; }
  .invitation-card { left: 523px; top: 47px; }

  .frame { fill: var(--paper); stroke: var(--red); }
  .ink { fill: var(--ink); }
  .red { fill: var(--red); }
  .outline {
    fill: var(--paper);
    stroke: var(--red);
    stroke-width: 1.6;
    font-weight: 300;
  }
  .rule { stroke: var(--red); stroke-width: 1; }
  .hairline { stroke: var(--ink); stroke-width: 0.8; }
  .checkbox { fill: none; stroke: var(--red); stroke-width: 1.8; }
</style>
</head>
<body>
<main class="suite">

  <!-- Response card -->
  <svg class="card rsvp-card" width="282" height="293" viewBox="0 0 282 293" aria-label="Response card">
    <rect class="frame" x="3" y="3" width="276" height="287" stroke-width="6"/>
    <text class="outline" x="19" y="66" font-size="80" textLength="238" lengthAdjust="spacingAndGlyphs">RSVP</text>
    <text class="ink" x="19" y="99" font-size="12.5" textLength="216" lengthAdjust="spacingAndGlyphs">BY THE TWENTY FIRST OF AUGUST</text>
    <text class="ink" x="19" y="122" font-size="16" textLength="216" lengthAdjust="spacingAndGlyphs">TWO THOUSAND THIRTEEN</text>
    <rect class="checkbox" x="21" y="172" width="25" height="23"/>
    <text class="ink" x="59" y="192" font-size="13">ACCEPT</text>
    <rect class="checkbox" x="150" y="172" width="25" height="23"/>
    <text class="ink" x="189" y="192" font-size="13">REGRETS</text>
    <text class="ink" x="19" y="245" font-size="12">NAMES:</text>
    <line class="hairline" x1="79" y1="245" x2="243" y2="245"/>
    <line class="hairline" x1="243" y1="241" x2="243" y2="249"/>
  </svg>

  <!-- Reception tag -->
  <svg class="card reception-tag" width="560" height="400" viewBox="0 0 560 400" aria-label="Reception card">
    <polygon class="frame" stroke-width="8" stroke-linejoin="miter"
             points="40,26 500,73 515,227 436,356 14,316"/>
    <g transform="rotate(6 40 26)">
      <text class="ink" x="75" y="77" font-size="19" letter-spacing="1.5">PLEASE JOIN US FOR</text>
      <text class="ink" x="75" y="106" font-size="19" letter-spacing="1.5">LUNCH AND DANCING</text>
      <text class="ink" x="75" y="134" font-size="19" font-weight="300" letter-spacing="2.5">following the service</text>
      <text class="ink" x="75" y="176" font-size="20">THE OLD MILL HOUSE</text>
      <text class="ink" x="75" y="204" font-size="20">2280 Willow Creek Road</text>
      <text class="ink" x="75" y="233" font-size="20" letter-spacing="1.5">Fairbrook, VA 22190</text>
      <text class="outline" x="60" y="300" font-size="66" textLength="348" lengthAdjust="spacingAndGlyphs">CELEBRATE</text>
    </g>
  </svg>

  <!-- Main invitation -->
  <svg class="card invitation-card" width="640" height="641" viewBox="0 0 640 641" aria-label="Bar Mitzvah invitation">
    <rect class="frame" x="5" y="5" width="630" height="631" stroke-width="10"/>
    <text class="ink" x="53" y="86" font-size="25" textLength="546" lengthAdjust="spacingAndGlyphs">IT IS WITH GREAT PRIDE AND JOY THAT</text>
    <text class="ink" x="53" y="127" font-size="25" textLength="546" lengthAdjust="spacingAndGlyphs">WE INVITE YOU TO JOIN US AS OUR SON</text>
    <text class="outline" x="53" y="280" font-size="182" stroke-width="2.4" textLength="546" lengthAdjust="spacingAndGlyphs">ETHAN</text>
    <text class="red" x="53" y="329" font-size="37" textLength="546" lengthAdjust="spacingAndGlyphs">CELEBRATES HIS BAR MITZVAH</text>

    <text class="ink" x="53" y="389" font-size="38" textLength="193" lengthAdjust="spacingAndGlyphs">SATURDAY</text>
    <text class="ink" x="53" y="419" font-size="14" textLength="193" lengthAdjust="spacingAndGlyphs">SEPTEMBER TWENTY EIGHT</text>
    <text class="ink" x="53" y="435" font-size="14" textLength="193" lengthAdjust="spacingAndGlyphs">TWO THOUSAND THIRTEEN</text>
    <text class="ink" x="53" y="475" font-size="38" textLength="105" lengthAdjust="spacingAndGlyphs">10.30</text>
    <text class="ink" x="173" y="455" font-size="14">IN THE</text>
    <text class="ink" x="173" y="471" font-size="14">MORNING</text>

    <text class="ink" x="336" y="376" font-size="17" textLength="261" lengthAdjust="spacingAndGlyphs">EASTBROOK VALLEY HEBREW</text>
    <text class="ink" x="336" y="411" font-size="36" textLength="261" lengthAdjust="spacingAndGlyphs">CONGREGATION</text>
    <text class="ink" x="336" y="435" font-size="17" textLength="261" lengthAdjust="spacingAndGlyphs">1520 LINDEN AVENUE ASHFORD</text>
    <text class="ink" x="336" y="472" font-size="32" textLength="261" lengthAdjust="spacingAndGlyphs">VIRGINIA 20990</text>

    <text class="red" x="53" y="538" font-size="15" font-weight="500" textLength="543" lengthAdjust="spacingAndGlyphs">PLEASE JOIN US FOR KIDDUSH IMMEDIATELY FOLLOWING THE SERVICE</text>
    <line class="rule" x1="53" y1="557" x2="163" y2="557"/>
    <line class="rule" x1="53" y1="553" x2="53" y2="561"/>
    <text class="red" x="320" y="565" font-size="21" text-anchor="middle" textLength="305" lengthAdjust="spacingAndGlyphs">MARK AND MIRIAM STONE</text>
    <line class="rule" x1="485" y1="557" x2="597" y2="557"/>
    <line class="rule" x1="597" y1="553" x2="597" y2="561"/>
  </svg>

</main>
</body>
</html>
```